label for wine brand Vela Rubi

we are interested interested in designing a label for a red wine of Spanish origin that is modern, but at the same time classic. The style we are looking for is in line with Chilean wines. Labels of two bodies with colorful, metallic stamping, thinking in Asian markets. We accept labels with watermarks, artistic, original but that are made thinking that the product to sell is wine.

Target Market(s)

United States and Asia

Industry/Entity Type

Commercial

Font styles to use
Decorative
Script

Requirements
Must have
• elegant and modern style
Nice to have
• metal texts
Should not have
• Drawings of animals

```html
<!DOCTYPE html>
<html lang="en">
<head>
<meta charset="utf-8">
<title>Vela Rubi – Pinot Noir Reserva Label</title>
<link rel="stylesheet" href="https://fonts.googleapis.com/css2?family=Pinyon+Script&family=Montserrat:wght@500;600&display=swap">
<style>
  :root {
    --backdrop: #0b0b0b;
    --label-black: #1c1b1a;
    --label-edge: #2a2826;
    --gold: #d9b46e;
    --script-white: #f2f0ec;
    --sketch-grey: #4a4846;
  }
  * { margin: 0; padding: 0; box-sizing: border-box; }
  html, body {
    width: 846px;
    height: 1200px;
    overflow: hidden;
    background: var(--backdrop);
  }
  .canvas {
    position: relative;
    width: 846px;
    height: 1200px;
    display: flex;
    align-items: center;
    justify-content: center;
  }
  .wine-label {
    position: relative;
    width: 620px;
    height: 955px;
    background: linear-gradient(180deg, var(--label-edge) 0%, var(--label-black) 18%, var(--label-black) 82%, var(--label-edge) 100%);
    font-family: "Montserrat", sans-serif;
    color: var(--gold);
    text-align: center;
  }
  .origin {
    position: absolute;
    top: 88px;
    left: 0;
    right: 0;
    font-size: 30px;
    font-weight: 600;
    letter-spacing: 4px;
  }
  .vineyard-artwork {
    position: absolute;
    top: 300px;
    left: 90px;
    width: 440px;
    height: 380px;
    background: radial-gradient(ellipse at 50% 60%, var(--sketch-grey) 0%, rgba(74,72,70,0.45) 45%, rgba(28,27,26,0) 75%);
  }
  .brand-name {
    position: absolute;
    top: 218px;
    left: 0;
    right: 0;
    font-family: "Pinyon Script", cursive;
    font-size: 92px;
    font-weight: 400;
    color: var(--script-white);
    line-height: 1;
  }
  .varietal {
    position: absolute;
    top: 680px;
    left: 0;
    right: 0;
    font-size: 36px;
    font-weight: 500;
    letter-spacing: 2px;
  }
  .classification {
    position: absolute;
    top: 772px;
    left: 0;
    right: 0;
    font-size: 34px;
    font-weight: 500;
    letter-spacing: 14px;
    padding-left: 14px;
  }
  .vintage {
    position: absolute;
    top: 850px;
    left: 0;
    right: 0;
    font-size: 30px;
    font-weight: 600;
    letter-spacing: 3px;
  }
</style>
</head>
<body>
  <main class="canvas">
    <section class="wine-label">
      <p class="origin">SPAIN</p>
      <div class="vineyard-artwork" role="img" aria-label="Line sketch of a grape cluster above a rustic vineyard farmhouse with trees"></div>
      <h1 class="brand-name">Vela Rubi</h1>
      <p class="varietal">PINOT NOIR</p>
      <p class="classification">RESERVA</p>
      <p class="vintage">2014</p>
    </section>
  </main>
</body>
</html>
```